Stationery Design Project

Would like to have the design elements we created in for our website (www.brook-holdings.example), incorporated in a stationery design layout.
Updates
Colors used in the logo attachments do not need to be used. We are open to different color variations. Looking for a crisp, clean, modern update using the design elements in attachments and which can also be viewed on or website.
A note to designers:
Project Deadline Extended
Reason: Due to update in our project description and requirements, we have decided to extend the deadline of this project to provide ample opportunity to all designers participating .
Requirements
Must have
- Must have continuity with the theme and design features used in our website. Have attached .jpg images of some of the design elements.

```html
<!DOCTYPE html>
<html lang="en">
<head>
<meta charset="utf-8">
<title>Brook Holdings Letterhead</title>
<link rel="stylesheet" href="https://fonts.googleapis.com/css2?family=Jost:wght@400&family=PT+Serif:wght@400&display=swap">
<style>
  :root {
    --paper: #ffffff;
    --ink: #2a2a2a;
    --grey: #8a8a8a;
    --green: #50b848;
    --blue: #0fa0e0;
    --blue-text: #1a9ad6;
  }
  * { margin: 0; padding: 0; box-sizing: border-box; }
  html, body {
    width: 948px;
    height: 1200px;
    overflow: hidden;
    background: var(--paper);
  }
  .letterhead {
    position: relative;
    width: 948px;
    height: 1200px;
    background: var(--paper);
  }
  .accent-bar-top {
    position: absolute;
    left: 0; top: 0;
    width: 296px; height: 22px;
    background: var(--green);
  }
  .brand-name {
    position: absolute;
    left: 52px; top: 92px;
    font-family: "Jost", sans-serif;
    font-weight: 400;
    font-size: 38px;
    letter-spacing: 1px;
    color: var(--ink);
  }
  .footer-company {
    position: absolute;
    left: 514px; top: 1094px;
  }
  .footer-company .company-name {
    font-family: "Jost", sans-serif;
    font-weight: 400;
    font-size: 16px;
    color: var(--blue-text);
    line-height: 20px;
  }
  .footer-company .address {
    font-family: "PT Serif", serif;
    font-size: 12.5px;
    color: var(--grey);
    line-height: 15px;
    font-style: normal;
  }
  .footer-divider {
    position: absolute;
    left: 712px; top: 1097px;
    width: 1px; height: 50px;
    background: var(--green);
  }
  .footer-contact {
    position: absolute;
    left: 727px; top: 1095px;
    list-style: none;
    font-family: "PT Serif", serif;
    font-size: 12.5px;
    line-height: 18.5px;
  }
  .footer-contact .label {
    display: inline-block;
    width: 24px;
    color: var(--blue-text);
    font-size: 11px;
  }
  .footer-contact .value { color: var(--grey); }
  .accent-bar-bottom {
    position: absolute;
    left: 0; top: 1180px;
    width: 948px; height: 20px;
    background: var(--blue);
  }
</style>
</head>
<body>
  <main class="letterhead">
    <div class="accent-bar-top"></div>
    <div class="brand-name">Brook</div>

    <div class="footer-company">
      <div class="company-name">Brook Holdings, Inc.</div>
      <address class="address">418 Alder Mill Road Suite 12<br>Marlow, GA 30999</address>
    </div>

    <div class="footer-divider"></div>

    <ul class="footer-contact">
      <li><span class="label">[P]</span><span class="value">(555) 014-2230</span></li>
      <li><span class="label">[F]</span><span class="value">(555) 014-2231</span></li>
      <li><span class="label">[E]</span><span class="value">info@brook-holdings.example</span></li>
    </ul>

    <div class="accent-bar-bottom"></div>
  </main>
</body>
</html>
```